Computer screen desktop background design for dentists orthodontic office PCs

We need a new design to use as the Windows desktop background picture for the PC workstations in a dentists orthodontic office.
The design should be vector graphics.
The aspect ratio should reflect the monitor size (Resolution: 1920x1200).
In the uploaded files you can find the logo, the fonts and the design of the business card.
The design should not be brighter than the Windows 10 background picture (monitor lifetime).

The office logo must be the dominating part of the design (see uploaded files).

You don't need to use the same fonts, but the used fonts have to be in harmony with the fonts used in the logo and the business card.
The colors used have to be in harmony with the logo.
All the text below must be on the design.
The logical text groups are separated by empty lines.

Kieferorthopädie Brunnweid

Dr. med. dent. Anton Vrabec
Fachzahnarzt für Kieferorthopädie (CH) (Important information!)

Please make something cool and modern that attracts the patient's attraction when seen on the monitor screen.

Target Market(s)

dentists orthodontic office

Industry/Entity Type

Computer

Font styles to use
Sans Serif

Colors

Designer to choose colors to be used in the design.

Requirements
Must have
• The design should be vector graphics.
• The aspect ratio should reflect the monitor size (Resolution: 1920x1200).
• In the uploaded files you can find the logo, the fonts and the design of the business card.
• The design should not be brighter than the Windows 10 background picture (monitor lifetime).
• The office logo must be the dominating part of the design (see uploaded files).
• You don't need to use the same fonts, but the used fonts have to be in harmony with the fonts used in the logo and the business card.
• The colors used have to be in harmony with the logo.
• All the text below must be on the design.
• The logical text groups are separated by empty lines.
• Kieferorthopädie Brunnweid
• Dr. med. dent. Anton Vrabec
• Fachzahnarzt für Kieferorthopädie (CH) (Important information!)
• Adobe Illustrator source files
Nice to have
• Please make something cool and modern that attracts the patient's attraction when seen on the monitor screen.
Should not have

```html
<!DOCTYPE html>
<html lang="de">
<head>
<meta charset="utf-8">
<title>Kieferorthopädie Brunnweid – Desktop</title>
<link rel="stylesheet" href="https://fonts.googleapis.com/css2?family=Roboto:wght@500;700&family=Open+Sans:wght@400;700&display=swap">
<style>
  :root {
    --stage: #a9a4e0;
    --navy: #1d1a5c;
    --navy-deep: #17144d;
    --wave-a: #23408f;
    --wave-b: #2b5aa8;
    --white: #ffffff;
    --accent: #1aa3e8;
    --soft: #d8dcf0;
  }
  html, body {
    margin: 0;
    width: 1200px;
    height: 470px;
    overflow: hidden;
    background: var(--stage);
  }
  .wallpaper {
    position: absolute;
    left: 240px;
    top: 10px;
    width: 720px;
    height: 450px;
    background: radial-gradient(ellipse at 30% 20%, #26226a 0%, var(--navy) 55%, var(--navy-deep) 100%);
    overflow: hidden;
    box-shadow: 0 6px 18px rgba(40, 30, 100, 0.35);
  }
  .wave-band {
    position: absolute;
    left: 0;
    top: 140px;
    width: 720px;
    height: 310px;
  }
  .brand-mark {
    position: absolute;
    left: 0;
    top: 90px;
    width: 720px;
    display: flex;
    justify-content: center;
    align-items: center;
    gap: 14px;
    font-family: "Roboto", sans-serif;
    font-weight: 700;
    font-size: 44px;
    color: var(--white);
  }
  .brand-mark .dot {
    width: 34px;
    height: 34px;
    border-radius: 50%;
    background: var(--accent);
  }
  .practice-name {
    position: absolute;
    left: 0;
    top: 264px;
    width: 720px;
    text-align: center;
    margin: 0;
    font-family: "Roboto", sans-serif;
    font-weight: 700;
    font-size: 24px;
    color: var(--white);
  }
  .doctor {
    position: absolute;
    left: 0;
    top: 320px;
    width: 720px;
    text-align: center;
    font-family: "Open Sans", sans-serif;
  }
  .doctor-name {
    margin: 0;
    font-weight: 700;
    font-size: 12.5px;
    color: var(--accent);
    text-transform: uppercase;
    letter-spacing: 0.2px;
  }
  .doctor-title {
    margin: 1px 0 0;
    font-weight: 400;
    font-size: 10px;
    color: var(--soft);
  }
</style>
</head>
<body>
  <main class="wallpaper">
    <svg class="wave-band" viewBox="0 0 720 310" role="img" aria-label="Flowing blue wave lines sweeping across the background">
      <defs>
        <linearGradient id="waveFill" x1="0" y1="0" x2="1" y2="1">
          <stop offset="0" stop-color="var(--wave-b)" stop-opacity="0.55"/>
          <stop offset="0.6" stop-color="var(--wave-a)" stop-opacity="0.35"/>
          <stop offset="1" stop-color="var(--wave-a)" stop-opacity="0.15"/>
        </linearGradient>
      </defs>
      <path d="M0 0 C120 40 220 190 420 230 C560 255 650 200 720 150 L720 310 L0 310 Z" fill="url(#waveFill)"/>
    </svg>

    <div class="brand-mark"><span class="dot"></span><span>Brunnweid</span></div>

    <h1 class="practice-name">Kieferorthopädie Brunnweid</h1>

    <div class="doctor">
      <p class="doctor-name">Dr. med. dent. Anton Vrabec</p>
      <p class="doctor-title">Fachzahnarzt für Kieferorthopädie (CH)</p>
    </div>
  </main>
</body>
</html>
```